Home page for Mira Talk Hub

Develop the home page for MiraTalkHub.co, which is an AI-powered chatbot platform that allows users to add an educated chatbot to their websites to assist customers with questions and other inquiries.

The hero banner should contain the text:

"Instantly create a FREE AI Chatbot for your website! Just enter the URL of your website below and the chatbot will educate itself about your business"

Below this text should be an text box to enter the URL of the visitor's website.

The platform is a subsidiary of KorvanPro.com, so the theme should be very similar to the website korvanpro.com.

I have attached the content for the page, a mockup of the hero banner section, and videos for the hero banner.

```html
<!DOCTYPE html>
<html lang="en">
<head>
<meta charset="utf-8">
<title>Mira Talk Hub — Home</title>
<link rel="stylesheet" href="https://fonts.googleapis.com/css2?family=Source+Sans+3:wght@400;600;700;900&display=swap">
<style>
:root{
  --navy:#1c3553;
  --navy-deep:#132a40;
  --blue:#5b95f9;
  --blue-soft:#dbe7fd;
  --ink:#1d2733;
  --muted:#4c5866;
  --white:#ffffff;
  --line:#e6ebf2;
}
*{box-sizing:border-box;margin:0;padding:0}
html,body{width:1200px;height:3124px;overflow:hidden;background:var(--white)}
body{position:relative;font-family:"Source Sans 3",sans-serif;color:var(--ink)}
.abs{position:absolute}
.hero-photo{left:0;top:0;width:1200px;height:690px;background:radial-gradient(ellipse at 60% 40%,#2a4256 0%,#1b3042 45%,#102233 100%)}
.hero-wave{left:0;top:580px;width:1200px;height:120px}
.nav{left:182px;top:0;width:836px;height:61px;background:var(--navy);border-radius:0 0 16px 16px;display:flex;align-items:center;padding:0 18px}
.brand{color:var(--white);font-size:22px;font-weight:600;white-space:nowrap}
.nav-links{display:flex;gap:20px;margin-left:auto;font-size:10px;color:#dfe7f2;white-space:nowrap}
.nav-sep{width:1px;height:26px;background:#5e7188;margin:0 18px 0 56px}
.btn-login{font-size:10px;font-weight:600;color:var(--white);border:1px solid var(--white);border-radius:3px;padding:6px 16px}
.btn-signup{font-size:10px;font-weight:600;color:var(--white);background:var(--blue);border-radius:3px;padding:7px 16px;margin-left:14px}
.hero-title{left:0;width:1200px;top:204px;text-align:center;color:var(--white);font-size:31px;line-height:39px;font-weight:400}
.hero-title b{font-weight:700}
.rule{height:3px;width:74px;background:var(--blue)}
.hero-sub{left:0;width:1200px;top:335px;text-align:center;color:#e6edf5;font-size:10.5px}
.url-input{left:406px;top:360px;width:387px;height:26px;background:rgba(255,255,255,.16);border-radius:2px;color:#d7e0ea;font-size:9.5px;padding:7px 13px}
.cta{background:var(--blue);color:var(--white);font-weight:600;border-radius:3px;text-align:center}
.eyebrow{color:var(--blue);font-size:9px;font-weight:700;text-transform:uppercase}
.h2{font-size:17px;font-weight:400;color:var(--ink)}
.h2 em{font-style:normal;color:var(--blue)}
.p{font-size:10.5px;line-height:18px;color:var(--muted)}
.p strong{color:var(--ink);font-weight:600}
.why{left:182px;top:1208px;width:836px;height:367px;background:var(--blue);border-radius:16px}
.why-panel{left:182px;top:1208px;width:836px;height:356px;background:var(--navy);border-radius:16px;overflow:hidden}
.why-texture{inset:0;background:radial-gradient(ellipse at 30% 60%,rgba(80,110,140,.22),transparent 60%),radial-gradient(ellipse at 70% 30%,rgba(80,110,140,.18),transparent 55%)}
.benefit{top:1372px;width:241px;height:86px;background:var(--blue);border-radius:13px;color:var(--white);font-size:12px;font-weight:700;line-height:19px;display:flex;align-items:center;justify-content:center;text-align:center;padding:0 26px}
.center{left:0;width:1200px;text-align:center}
.step-title{font-size:12.5px;font-weight:700;color:var(--ink)}
.ticks{list-style:none}
.ticks li{position:relative;padding-left:15px;font-size:10px;line-height:15px;color:var(--ink);font-weight:600;margin-bottom:6px}
.ticks li::before{content:"";position:absolute;left:0;top:3px;width:9px;height:9px;border-radius:50%;background:var(--blue)}
.ticks li::after{content:"";position:absolute;left:2.5px;top:5px;width:3px;height:2px;border-left:1.3px solid #fff;border-bottom:1.3px solid #fff;transform:rotate(-45deg)}
.num{font-size:104px;font-weight:900;color:var(--blue);letter-spacing:2px}
.step-ornament{width:40px;height:44px;border-radius:8px;background:linear-gradient(160deg,var(--blue-soft),#eef4fe)}
.feature{top:2834px;width:263px;height:245px;background:var(--white);border-radius:14px;box-shadow:0 2px 12px rgba(30,50,80,.08);text-align:center;padding:0 22px}
.feature h3{font-size:12.5px;font-weight:700;margin-top:120px;color:var(--ink)}
.feature p{font-size:10px;line-height:17.5px;color:var(--muted);margin-top:10px}
.feature p b{color:var(--ink);font-weight:600}
.feature svg{position:absolute;left:50%;top:38px;transform:translateX(-50%)}
</style>
</head>
<body>

<div class="abs hero-photo" role="img" aria-label="Dim blurred photo of robotic machinery in navy tones"></div>
<svg class="abs hero-wave" viewBox="0 0 1200 120" preserveAspectRatio="none" aria-hidden="true">
  <path d="M0 95 C150 40 300 10 430 14 C620 20 760 92 1200 60 L1200 120 L0 120Z" fill="#5b95f9"/>
  <path d="M0 101 C150 55 300 28 430 32 C640 40 780 112 1200 80 L1200 120 L0 120Z" fill="#ffffff"/>
</svg>

<header class="abs nav">
  <div class="brand">Mira Talk Hub</div>
  <nav class="nav-links"><span>About Us</span><span>Learn More</span><span>Affiliate Program</span><span>History of AI</span><span>Pricing</span><span>Blog</span></nav>
  <div class="nav-sep"></div>
  <span class="btn-login">Login</span>
  <span class="btn-signup">Sign Up</span>
</header>

<h1 class="abs hero-title">Instantly create a FREE AI <b>Chatbot</b><br>for your website!</h1>
<div class="abs rule" style="left:563px;top:296px"></div>
<p class="abs hero-sub">Just enter the URL of your website below and the chatbot will educate itself about your business.</p>
<div class="abs url-input">Enter your URL here...</div>
<div class="abs cta" style="left:406px;top:397px;width:387px;height:26px;font-size:9.5px;line-height:26px">Build my free website now!</div>

<section>
  <div class="abs eyebrow" style="left:182px;top:812px">Welcome to Mira Talk Hub</div>
  <h2 class="abs h2" style="left:182px;top:830px">Your Business’s Ultimate <em>AI Assistant</em>!</h2>
  <div class="abs rule" style="left:182px;top:865px"></div>
  <p class="abs p" style="left:182px;top:901px;width:420px"><strong>Imagine having a tireless assistant that’s always ready to interact with your customers, answer their questions, and guide them through their journey on your website.</strong></p>
  <p class="abs p" style="left:182px;top:953px;width:412px">Meet Mira Talk Hub – the fastest and easiest way to create an intelligent AI Agent for your business in just a few minutes. Whether you’re a small business owner, a growing enterprise or a digital agency, Mira Talk Hub is here to revolutionize customer support for you.</p>
  <div class="abs cta" style="left:182px;top:1041px;width:150px;height:27px;font-size:9.5px;line-height:27px">Build my free website now!</div>
  <svg class="abs" style="left:700px;top:790px" width="360" height="300" aria-hidden="true">
    <circle cx="147" cy="137" r="130" fill="#5b95f9"/>
    <circle cx="136" cy="127" r="130" fill="#1c3553"/>
    <circle cx="35" cy="36" r="15" fill="#5b95f9"/>
  </svg>
  <div class="abs" role="img" aria-label="Illustration of a white robot reading a red book" style="left:760px;top:752px;width:170px;height:378px;border-radius:60px;background:linear-gradient(180deg,#e9edf2,#c4ccd6 60%,#e5e9ee)"></div>
</section>

<section>
  <div class="abs why"></div>
  <div class="abs why-panel"><div class="abs why-texture" role="img" aria-label="Faint background photo of people working with technology"></div></div>
  <div class="abs eyebrow center" style="top:1243px">Why choose Mira Talk Hub?</div>
  <h2 class="abs center" style="top:1260px;color:#fff;font-size:17.5px;font-weight:400;line-height:23px">Mira Talk Hub isn’t just another chatbot.<br>It’s a customizable, smart, and scalable solution designed.</h2>
  <div class="abs rule" style="left:563px;top:1318px"></div>
  <div class="abs benefit" style="left:218px">Enhance Your Customer Support 24/7</div>
  <div class="abs benefit" style="left:479px">Save Your Time by Automating Repetitive Inquiries</div>
  <div class="abs benefit" style="left:740px">Improve Customer Satisfaction and Engagement</div>
  <p class="abs center" style="top:1492px;color:#fff;font-size:10px;font-weight:600;line-height:18px">With Mira Talk Hub, you’ll have a personalized assistant that grows smarter over time, helping you deliver exceptional service to every customer.<br>Let’s dive into how easy it is to set up and unleash the power of AI for your business</p>
</section>

<section>
  <div class="abs eyebrow center" style="top:1648px">How it works?</div>
  <h2 class="abs h2 center" style="top:1665px">The 3 Simple Steps to Launch Your <em>Mira Talk Hub</em>.</h2>
  <div class="abs rule" style="left:563px;top:1702px"></div>

  <svg class="abs" style="left:0;top:1740px" width="1200" height="920" aria-hidden="true">
    <path d="M372 286 C380 340 420 345 560 330 C700 315 780 300 805 330" fill="none" stroke="#9ebff8" stroke-width="1.2" stroke-dasharray="5 4"/>
    <path d="M805 600 C790 650 700 625 560 620 C420 615 380 625 372 650" fill="none" stroke="#9ebff8" stroke-width="1.2" stroke-dasharray="5 4"/>
    <circle cx="392" cy="154" r="130" fill="#5b95f9"/><circle cx="381" cy="144" r="130" fill="#1c3553"/><circle cx="289" cy="47" r="15" fill="#5b95f9"/>
    <circle cx="816" cy="472" r="130" fill="#5b95f9"/><circle cx="805" cy="462" r="130" fill="#1c3553"/><circle cx="715" cy="364" r="15" fill="#5b95f9"/>
    <circle cx="392" cy="789" r="130" fill="#5b95f9"/><circle cx="381" cy="779" r="130" fill="#1c3553"/><circle cx="289" cy="683" r="15" fill="#5b95f9"/>
  </svg>
  <div class="abs step-ornament" role="img" aria-label="Small footsteps decoration" style="left:221px;top:1976px"></div>
  <div class="abs step-ornament" role="img" aria-label="Small footsteps decoration" style="left:932px;top:2294px"></div>
  <div class="abs step-ornament" role="img" aria-label="Small footsteps decoration" style="left:221px;top:2613px"></div>

  <div class="abs num" style="left:311px;top:1810px">01</div>
  <div class="abs num" style="left:735px;top:2128px">02</div>
  <div class="abs num" style="left:311px;top:2445px">03</div>

  <h3 class="abs step-title" style="left:568px;top:1792px">Educate Your Mira Talk Hub</h3>
  <p class="abs p" style="left:568px;top:1819px;width:405px">Enter the URL of your website, and let Mira Talk Hub do the heavy lifting. The bot will crawl your site and educate itself about your business. Choose from flexible crawling options:</p>
  <ul class="abs ticks" style="left:568px;top:1872px;width:410px">
    <li>Home Page Only: Ideal for a quick setup with basic information.</li>
    <li>Specific Sub-Pages: Focus on important sections like FAQs, pricing, or services.</li>
    <li>All Pages: For a comprehensive AI assistant that knows your business inside-out.</li>
  </ul>
  <p class="abs p" style="left:568px;top:1949px;width:405px">The more pages the bot crawls, the smarter it becomes, ensuring it provides accurate and helpful responses to your customers.</p>

  <h3 class="abs step-title" style="left:222px;top:2110px">Customize Your Mira Talk Hub</h3>
  <p class="abs p" style="left:222px;top:2137px">Make your bot uniquely yours! Personalize it by:</p>
  <ul class="abs ticks" style="left:222px;top:2173px;width:420px">
    <li>Giving it a name that represents your brand.</li>
    <li>Choosing an avatar to align with your website’s design.</li>
    <li>Uploading additional knowledge such as documents, spreadsheets, and FAQs to enrich its database.</li>
  </ul>
  <p class="abs p" style="left:222px;top:2267px;width:410px">The more information you provide, the smarter and more efficient your bot becomes in handling.</p>

  <h3 class="abs step-title" style="left:568px;top:2412px">Activate and Deploy Your Mira Talk Hub</h3>
  <p class="abs p" style="left:568px;top:2439px;width:410px">You’re just one step away from transforming your customer support experience! Here’s how you go live:</p>
  <ul class="abs ticks" style="left:568px;top:2492px;width:415px">
    <li>Enable the optional Human Assistance Mode, allowing you or your team to step in for direct customer interaction. Configure this feature manually or set a schedule, like business hours for personal assistance and after-hours AI responses.</li>
    <li>Copy the unique HTML code generated for your bot.</li>
    <li>Paste the code into your website.</li>
  </ul>
  <p class="abs p" style="left:568px;top:2599px;width:410px">And just like that, your Mira Talk Hub comes alive on your website, ready to interact with visitors and provide seamless support!</p>
</section>

<section>
  <div class="abs eyebrow center" style="top:2729px">Advanced features</div>
  <h2 class="abs h2 center" style="top:2745px">Advanced Features That Set <em>Mira Talk Hub</em> Apart.</h2>
  <div class="abs rule" style="left:563px;top:2782px"></div>

  <article class="abs feature" style="left:182px">
    <svg width="46" height="46" viewBox="0 0 46 46" fill="none" stroke="#5b95f9" stroke-width="1.6" aria-hidden="true"><path d="M12 32 C16 28 13 16 22 12 C31 9 36 18 35 26 L38 34 Z"/><path d="M20 33 a5 5 0 0 0 9 2"/><circle cx="23" cy="10" r="2"/><path d="M40 14 q3 5 0 10"/></svg>
    <h3>Real-Time Notifications</h3>
    <p>Stay on top of customer interactions with text and email alerts for new inquiries. Never miss a chance to connect with your customers whether you’re in the office or on the go.</p>
  </article>
  <article class="abs feature" style="left:468px">
    <svg width="46" height="48" viewBox="0 0 46 48" fill="none" stroke="#5b95f9" stroke-width="1.6" aria-hidden="true"><rect x="8" y="4" width="24" height="40" rx="3"/><circle cx="16" cy="18" r="3"/><path d="M11 28 q5 -6 10 0"/><path d="M18 32h16M18 36h12M24 11h16v10H24z"/><circle cx="37" cy="36" r="4"/></svg>
    <h3>Mobile App Access</h3>
    <p>Monitor your bot’s activity and interact with customers directly through our mobile app. Whether you’re at a meeting or traveling, you’re always connected.</p>
  </article>
  <article class="abs feature" style="left:756px">
    <svg width="50" height="50" viewBox="0 0 50 50" fill="none" stroke="#5b95f9" stroke-width="1.6" aria-hidden="true"><rect x="4" y="4" width="38" height="38" rx="3"/><path d="M4 12h38"/><circle cx="30" cy="8" r="1"/><circle cx="34" cy="8" r="1"/><circle cx="38" cy="8" r="1"/><path d="M10 20h26M10 28h26M10 36h14"/><circle cx="18" cy="20" r="2.5"/><circle cx="28" cy="28" r="2.5"/><path d="M32 32l4 14 3-5 6-1z"/></svg>
    <h3>Customizable Plans</h3>
    <p><b>Free Plan</b>: Perfect for smaller or newer businesses.<br><b>Business Plans</b>: Scaled for growing enterprises with advanced features.<br><b>Agency Plan</b>: Allows unlimited chatbot creation for digital agencies.</p>
  </article>
</section>

</body>
</html>
```